Healthcare Technology Company Business Card Design

Hi,

We require a new business card design thats catchy and professional.
Our target audience is healthcare professionals. See supplied artwork for our logo.

If you think its achievable please try add the tag line, not necessary however.
"Building smarter tools to support clinical teams and lift practice performance"

We'll require the following information on the card. No need to have the subject titles but i've referenced them for your convenience.

Personal Details
Mark Towler
Position: Director
Phone Number - 03 9471 5382
Mobile Number - 0427 836 259
Email: firstname.lastname@velkarin.com.au

Company Details
Suite 38, 216 Wendrell Street
Harlow Bay, Eastmere
Fax: 03 8214 3975
velkarin.com.au

Prefer a thinner design than the normal stock standard business card dimensions.
Please ensure there is adequate bleed.

Target Market(s)

Healthcare Professionals

Industry/Entity Type

Healthcare

Font styles to use
Sans Serif

Requirements
Must have
• Clean, Sharp Looks
Should not have
• Any healthcare symbols

```html
<!DOCTYPE html>
<html lang="en">
<head>
<meta charset="UTF-8">
<title>Velkarin Business Card</title>
<link rel="stylesheet" href="https://fonts.googleapis.com/css2?family=Arimo:wght@400;700&display=swap">
<style>
  :root {
    --page-bg: #d9d9d9;
    --card-light: #2c2c2d;
    --card-dark: #121212;
    --text-light: #ffffff;
    --rule: #bdbdbd;
    --plate: #ffffff;
    --brand-navy: #1d2a5c;
  }
  * { margin: 0; padding: 0; box-sizing: border-box; }
  html, body {
    width: 1200px; height: 1000px; overflow: hidden;
    background: var(--page-bg);
    font-family: "Arimo", Arial, sans-serif;
  }
  .canvas { position: relative; width: 1200px; height: 1000px; }
  .card {
    position: absolute; left: 280px; width: 640px; height: 400px;
    overflow: hidden; background: var(--card-light);
    color: var(--text-light);
  }
  .card--front { top: 70px; }
  .card--back { top: 530px; }
  .card__shade { position: absolute; inset: 0; width: 100%; height: 100%; }

  .brand-plate {
    position: absolute; left: 22px; top: 28px; width: 250px; height: 58px;
    background: var(--plate); border-radius: 9px;
    display: flex; align-items: center; padding-left: 22px; gap: 10px;
  }
  .brand-plate__mark { width: 18px; height: 18px; background: var(--brand-navy); }
  .brand-plate__name {
    font-weight: 700; font-size: 26px; color: var(--brand-navy); letter-spacing: 0.3px;
  }
  .divider {
    position: absolute; left: 330px; top: 28px; width: 1px; height: 305px;
    background: var(--rule);
  }
  .contact {
    position: absolute; font-size: 19px; line-height: 25px; letter-spacing: 0.4px;
  }
  .contact--personal { left: 34px; top: 122px; }
  .contact--company { left: 360px; top: 152px; }

  .wordmark {
    position: absolute; left: 0; right: 0; top: 120px; text-align: center;
    padding-left: 80px; font-size: 40px; font-weight: 400; letter-spacing: 4px;
  }
  .tagline {
    position: absolute; left: 18px; right: 18px; bottom: 38px;
    font-size: 13.5px; letter-spacing: 1.6px; text-align: center; white-space: nowrap;
  }
</style>
</head>
<body>
<main class="canvas">
  <section class="card card--front" aria-label="Business card front">
    <svg class="card__shade" viewBox="0 0 640 400" preserveAspectRatio="none" aria-hidden="true">
      <polygon points="0,345 640,95 640,400 0,400" fill="var(--card-dark)"/>
    </svg>
    <div class="brand-plate">
      <span class="brand-plate__mark"></span>
      <span class="brand-plate__name">Velkarin</span>
    </div>
    <div class="divider"></div>
    <p class="contact contact--personal">
      Mark Towler<br>
      Position: Director<br>
      Phone Number - 03 9471 5382<br>
      Mobile Number - 0427 836 259<br>
      Email: firstname.lastname@<br>
      velkarin.com.au
    </p>
    <p class="contact contact--company">
      Suite 38, 216 Wendrell Street<br>
      Harlow Bay, Eastmere<br>
      Fax: 03 8214 3975<br>
      velkarin.com.au
    </p>
  </section>

  <section class="card card--back" aria-label="Business card back">
    <svg class="card__shade" viewBox="0 0 640 400" preserveAspectRatio="none" aria-hidden="true">
      <polygon points="0,215 640,125 640,400 0,400" fill="var(--card-dark)"/>
    </svg>
    <h1 class="wordmark">Velkarin</h1>
    <p class="tagline">Building smarter tools to support clinical teams and lift practice performance</p>
  </section>
</main>
</body>
</html>
```